Business Card Design

I'm a fishing guide needing a clean, concise design for my business. I'd like to use the cover photo and font design from my website for the background of the business card. My website is:
www.tidewrenoutfitters.com

Industry/Entity Type

Business

Contact Information for Business Card

Capt. Dale Penrow
Fly, Light Tackle, Conventional Gear
Gamefish of Massachusetts
website: www.tidewrenoutfitters.com
cell: 508-461-2297
email: dale@tidewrenoutfitters.com

```html
<!DOCTYPE html>
<html lang="en">
<head>
<meta charset="utf-8">
<title>Tidewren Outfitters Business Card</title>
<link rel="stylesheet" href="https://fonts.googleapis.com/css2?family=Oswald:wght@300;400;700&display=swap">
<style>
  :root {
    --backdrop: #2b2b2d;
    --navy: #141632;
    --photo-light: #9aa1b4;
    --photo-mid: #5d6479;
    --photo-dark: #2f3346;
    --white: #ffffff;
    --soft-white: #e9eaf0;
  }
  html, body {
    margin: 0;
    width: 1200px;
    height: 1000px;
    overflow: hidden;
    background: var(--backdrop);
  }
  .card {
    position: absolute;
    left: 100px;
    top: 214px;
    width: 1000px;
    height: 572px;
    background: var(--navy);
    overflow: hidden;
    font-family: "Oswald", sans-serif;
    color: var(--white);
    box-shadow: 0 18px 40px rgba(0,0,0,0.45);
  }
  .card__photo {
    position: absolute;
    inset: 0;
  }
  .card__header {
    position: absolute;
    left: 0;
    right: 0;
    top: 26px;
    text-align: center;
  }
  .card__name {
    margin: 0;
    font-weight: 700;
    font-size: 42px;
    line-height: 58px;
    letter-spacing: 2px;
    text-transform: uppercase;
  }
  .card__tagline {
    margin: 8px 0 0;
    font-weight: 300;
    font-size: 25px;
    line-height: 36px;
    letter-spacing: 1.5px;
    color: var(--soft-white);
  }
  .brand {
    position: absolute;
    left: 70px;
    top: 440px;
    display: flex;
    align-items: center;
    gap: 16px;
  }
  .brand__mark {
    width: 22px;
    height: 22px;
    border-radius: 50%;
    background: var(--white);
  }
  .brand__name {
    font-weight: 400;
    font-size: 44px;
    letter-spacing: 1px;
    color: var(--white);
  }
  .contacts {
    position: absolute;
    left: 590px;
    top: 310px;
    list-style: none;
    margin: 0;
    padding: 0;
  }
  .contacts__item {
    display: flex;
    align-items: center;
    gap: 16px;
    height: 40px;
    font-weight: 300;
    font-size: 24px;
    letter-spacing: 0.5px;
  }
  .contacts__icon {
    width: 28px;
    height: 28px;
    flex: none;
  }
</style>
</head>
<body>
  <section class="card">
    <svg class="card__photo" width="1000" height="572" viewBox="0 0 1000 572" role="img" aria-label="Photo of an angler holding a large tuna with a fly in its mouth">
      <defs>
        <linearGradient id="photoTone" x1="0" y1="0" x2="1" y2="1">
          <stop offset="0" stop-color="var(--photo-mid)"/>
          <stop offset="0.45" stop-color="var(--photo-light)"/>
          <stop offset="1" stop-color="var(--photo-dark)"/>
        </linearGradient>
      </defs>
      <path d="M0 150 H1000 V290 H500 V415 H0 Z" fill="url(#photoTone)"/>
    </svg>

    <header class="card__header">
      <h1 class="card__name">Captain Dale Penrow</h1>
      <p class="card__tagline">Fly, Light Tackle, Conventional Gear Gamefish of Massachusetts</p>
    </header>

    <div class="brand">
      <span class="brand__mark"></span>
      <span class="brand__name">Tidewren Outfitters</span>
    </div>

    <ul class="contacts">
      <li class="contacts__item">
        <svg class="contacts__icon" viewBox="0 0 28 28" aria-hidden="true">
          <circle cx="14" cy="14" r="14" fill="var(--white)"/>
          <rect x="10" y="6" width="8" height="16" rx="1.5" fill="var(--navy)"/>
          <rect x="11.5" y="8" width="5" height="9" fill="var(--white)"/>
        </svg>
        508-461-2297
      </li>
      <li class="contacts__item">
        <svg class="contacts__icon" viewBox="0 0 28 28" aria-hidden="true">
          <circle cx="14" cy="14" r="14" fill="var(--white)"/>
          <rect x="7" y="9" width="14" height="10" fill="var(--navy)"/>
          <path d="M7 9 L14 15 L21 9" fill="none" stroke="var(--white)" stroke-width="1.4"/>
        </svg>
        dale@tidewrenoutfitters.com
      </li>
      <li class="contacts__item">
        <svg class="contacts__icon" viewBox="0 0 28 28" aria-hidden="true">
          <circle cx="14" cy="14" r="14" fill="var(--white)"/>
          <g fill="none" stroke="var(--navy)" stroke-width="1.5">
            <circle cx="14" cy="14" r="8"/>
            <ellipse cx="14" cy="14" rx="3.5" ry="8"/>
            <line x1="6" y1="14" x2="22" y2="14"/>
          </g>
        </svg>
        www.tidewrenoutfitters.com
      </li>
    </ul>
  </section>
</body>
</html>
```